Logo & Visitenkarte für Soziale Dienstleistungen, Beratung & Therapie
Zielgruppe
[frontside]
Konrad Wallmuth
Dipl. Sozialpädagoge (FH)
systemischer Einzel-, Paar- und Familientherapeut (VKTB)
Mobil: 0176 / 4 829 31 57
Mail: konrad-wallmuth@rundpost.de
'Soziale Dienstleistungen, Beratung & Therapie' [slogan]
[social services, counseling & therapy]
'systemische Beratung & Therapie,
ambulante Hilfen zur Erziehung, intensive Familienberatung, aufsuchende Familientherapie
soziale Projekte, Erwachsenenbildung, Lehraufträge' [business offers - backside of the card]
Zielgruppen [traget groups]:
Familien, Kinder- und Jugendliche, Einzelpersonen, Netzwerkpartner,
Institutionen, Ämter, Schulen, Kliniken, etc.

```html
<!DOCTYPE html>
<html lang="de">
<head>
<meta charset="utf-8">
<title>Visitenkarte – Soziale Dienstleistungen, Beratung &amp; Therapie</title>
<link rel="stylesheet" href="https://fonts.googleapis.com/css2?family=Fira+Sans+Condensed:wght@300;400;500&display=swap">
<style>
  :root {
    --backdrop: #c6c5c0;
    --paper: #ffffff;
    --teal: #5e8f89;
    --teal-light: #a9cbc2;
    --ink: #4b5053;
  }
  * { margin: 0; padding: 0; box-sizing: border-box; }
  html, body { width: 900px; height: 1200px; overflow: hidden; }
  body {
    background: var(--backdrop);
    font-family: "Fira Sans Condensed", "Arial Narrow", sans-serif;
    color: var(--ink);
    position: relative;
  }
  .card {
    position: absolute;
    left: 70px;
    width: 760px;
    height: 492px;
  }
  .card--front { top: 78px; background: var(--paper); }
  .card--back { top: 630px; background: var(--teal); }

  .brand {
    position: absolute;
    left: 70px;
    top: 46px;
    display: flex;
    flex-direction: column;
    gap: 14px;
  }
  .brand__square {
    width: 44px;
    height: 44px;
    background: var(--teal);
  }
  .brand__name {
    font-weight: 400;
    font-size: 26px;
    color: var(--teal);
    letter-spacing: 0.02em;
  }
  .slogan {
    position: absolute;
    left: 230px;
    top: 40px;
    font-weight: 300;
    font-size: 29px;
    line-height: 38px;
    color: var(--ink);
  }
  .contact {
    position: absolute;
    left: 367px;
    top: 228px;
    font-weight: 300;
    font-size: 23px;
    line-height: 31px;
  }
  .contact__name {
    font-weight: 500;
    color: var(--teal);
  }
  .contact__lines { margin-bottom: 12px; }
  .contact__row { display: flex; }
  .contact__label { width: 72px; }

  .back-brand {
    position: absolute;
    inset: 0;
    display: flex;
    align-items: center;
    justify-content: center;
    gap: 26px;
  }
  .back-brand__square {
    width: 70px;
    height: 70px;
    background: var(--teal-light);
  }
  .back-brand__name {
    font-weight: 400;
    font-size: 76px;
    color: var(--paper);
    letter-spacing: 0.02em;
  }
</style>
</head>
<body>
  <section class="card card--front">
    <div class="brand">
      <span class="brand__square"></span>
      <span class="brand__name">Wallmuth</span>
    </div>
    <p class="slogan">Soziale Dienstleistungen,<br>Beratung &amp; Therapie</p>
    <div class="contact">
      <p class="contact__name">Konrad Wallmuth</p>
      <p class="contact__lines">Dipl. Sozialpädagoge (FH)<br>systemischer Einzel-, Paar-<br>und Familientherapeut (VKTB)</p>
      <p class="contact__row"><span class="contact__label">Mobil:</span><span>0176 / 4 829 31 57</span></p>
      <p class="contact__row"><span class="contact__label">Mail:</span><span>konrad-wallmuth@rundpost.de</span></p>
    </div>
  </section>

  <section class="card card--back">
    <div class="back-brand">
      <span class="back-brand__square"></span>
      <span class="back-brand__name">Wallmuth</span>
    </div>
  </section>
</body>
</html>
```